Ferncliff Capital needs Brochure design for Trading System

We need a brochure design that improves what we have. Take our words and emhance the layout etc. The project needs to be easily editable becuaes we will need to update statistics etc. The look should be very professional for institutional clients.

```html
<!DOCTYPE html>
<html lang="en">
<head>
<meta charset="utf-8">
<title>Ferncliff Capital – ClearviewML Brochure Covers</title>
<link href="https://fonts.googleapis.com/css2?family=Didact+Gothic&family=Open+Sans:ital,wght@0,400;0,700;1,700&display=swap" rel="stylesheet">
<style>
  :root {
    --stage: #a3a3a3;
    --paper: #ffffff;
    --ink-dark: #1c1d20;
    --band-dark: #2a2b2f;
    --band-mid: #3b3c41;
    --sky-light: #dde9f4;
    --glass-blue: #3f5f9e;
    --glass-deep: #1f3466;
    --text-light: #ffffff;
    --text-soft: #d6d8dc;
    --brand-grey: #3a3a3a;
    --accent-blue: #4a6fb0;
  }
  * { box-sizing: border-box; margin: 0; padding: 0; }
  html, body { width: 1200px; height: 2691px; overflow: hidden; }
  body {
    background: var(--stage);
    font-family: "Didact Gothic", "Century Gothic", sans-serif;
    position: relative;
  }
  .slot {
    position: absolute;
    left: 0;
    width: 1200px;
    height: 897px;
    display: flex;
    align-items: center;
    justify-content: center;
  }
  .slot--cover { top: 0; }
  .slot--back { top: 897px; }
  .slot--spread { top: 1794px; }

  .page {
    position: relative;
    width: 1000px;
    height: 708px;
    overflow: hidden;
    box-shadow: 0 14px 30px rgba(0,0,0,0.25);
  }

  /* Front cover */
  .cover { background: var(--paper); }
  .cover__header {
    position: absolute; top: 0; left: 0; right: 0; height: 112px;
    background: linear-gradient(180deg, #ffffff 0%, #f1f4f8 100%);
    display: flex; justify-content: space-between; align-items: center;
    padding: 0 56px;
    z-index: 2;
  }
  .brand { display: flex; align-items: center; gap: 14px; color: var(--brand-grey); }
  .brand__mark { width: 38px; height: 38px; background: var(--ink-dark); }
  .brand__name { font-size: 34px; letter-spacing: 2px; line-height: 1; }
  .brand__sub { font-size: 13px; letter-spacing: 5px; margin-top: 6px; }
  .partner { display: flex; align-items: center; gap: 12px; color: var(--brand-grey); }
  .partner__mark { width: 34px; height: 34px; border-radius: 50%; background: var(--accent-blue); }
  .partner__name { font-size: 30px; line-height: 1; }
  .partner__sub { font-size: 13px; margin-top: 4px; }

  .cover__photo {
    position: absolute; top: 112px; left: 0; right: 0; height: 398px;
    background:
      linear-gradient(100deg, var(--glass-deep) 0%, var(--glass-blue) 28%, var(--sky-light) 48%, var(--sky-light) 55%, var(--glass-blue) 72%, var(--glass-deep) 100%);
  }
  .cover__title-band {
    position: absolute; top: 510px; left: 0; right: 0; height: 64px;
    background: var(--ink-dark);
    display: flex; align-items: center; justify-content: center;
  }
  .cover__title {
    font-family: "Open Sans", sans-serif; font-weight: 700;
    font-size: 38px; line-height: 1; color: var(--text-light); letter-spacing: 1px;
  }
  .cover__footer {
    position: absolute; top: 574px; left: 0; right: 0; bottom: 0;
    background: linear-gradient(180deg, var(--band-mid) 0%, var(--band-dark) 100%);
    text-align: center; color: var(--text-soft);
    padding-top: 22px;
  }
  .cover__tagline { font-size: 22px; line-height: 1.2; letter-spacing: 0.5px; }
  .cover__rule { width: 820px; margin: 14px auto 12px; border-top: 1px dotted #8a8c92; }
  .cover__web { font-size: 17px; line-height: 1.2; display: inline-flex; align-items: center; gap: 10px; }

  /* Back cover */
  .back {
    background: var(--ink-dark);
    color: var(--text-light);
    text-align: center;
  }
  .back__photo {
    position: absolute; inset: 0;
    background: radial-gradient(ellipse at 50% 45%, #4a4644 0%, #2b2a2b 45%, #151618 100%);
  }
  .back__content { position: relative; padding-top: 70px; }
  .back__thanks {
    font-family: "Open Sans", sans-serif; font-style: italic; font-weight: 700;
    font-size: 54px; line-height: 1.2;
  }
  .back__company { font-size: 26px; line-height: 1.2; margin-top: 270px; letter-spacing: 0.5px; }
  .back__rule { width: 340px; margin: 12px auto 14px; border-top: 1px dotted #b8b8b8; }
  .back__line { font-size: 17px; line-height: 1.2; color: var(--text-soft); margin: 6px 0; }
  .back__icon { display: block; margin: 10px auto 4px; }
  .back__phone { font-family: "Open Sans", sans-serif; font-weight: 700; font-size: 19px; line-height: 1.2; }

  /* Spread */
  .spread {
    width: 1000px; height: 354px; display: flex;
    box-shadow: 0 14px 30px rgba(0,0,0,0.25);
  }
  .spread__half { width: 500px; height: 354px; overflow: hidden; position: relative; }
  .spread__half .page { transform: scale(0.5); transform-origin: 0 0; box-shadow: none; }
</style>
</head>
<body>

<section class="slot slot--cover">
  <article class="page cover">
    <header class="cover__header">
      <div class="brand">
        <span class="brand__mark"></span>
        <div><div class="brand__name">FERNCLIFF</div><div class="brand__sub">CAPITAL MANAGEMENT</div></div>
      </div>
      <div class="partner">
        <span class="partner__mark"></span>
        <div><div class="partner__name">QDS</div><div class="partner__sub">Quantis Data Systems</div></div>
      </div>
    </header>
    <div class="cover__photo" role="img" aria-label="Photograph looking up at glass skyscrapers against a pale sky"></div>
    <div class="cover__title-band"><h1 class="cover__title">CLEARVIEWML</h1></div>
    <footer class="cover__footer">
      <p class="cover__tagline">Bringing together expert capital management and agile predictive modeling</p>
      <div class="cover__rule"></div>
      <p class="cover__web">
        <svg width="16" height="16" viewBox="0 0 16 16"><circle cx="8" cy="8" r="7" fill="none" stroke="#d6d8dc" stroke-width="1.4"/><path d="M1 8h14M8 1c3 3 3 11 0 14M8 1c-3 3-3 11 0 14" fill="none" stroke="#d6d8dc" stroke-width="1.2"/></svg>
        www.ferncliffcm.com
      </p>
    </footer>
  </article>
</section>

<section class="slot slot--back">
  <article class="page back">
    <div class="back__photo" role="img" aria-label="Dark photograph of two business people shaking hands"></div>
    <div class="back__content">
      <h2 class="back__thanks">Thank you!</h2>
      <p class="back__company">Ferncliff Capital Management</p>
      <div class="back__rule"></div>
      <p class="back__line">desk@ferncliffcm.com</p>
      <svg class="back__icon" width="18" height="13" viewBox="0 0 18 13"><rect x="1" y="1" width="16" height="11" fill="none" stroke="#fff" stroke-width="1.4"/><path d="M1 1l8 6 8-6" fill="none" stroke="#fff" stroke-width="1.4"/></svg>
      <p class="back__line">office@ferncliffcm.com</p>
      <svg class="back__icon" width="16" height="16" viewBox="0 0 16 16"><path d="M4 1l3 3-2 2c1 2 3 4 5 5l2-2 3 3-2 3C7 15 1 9 1 3z" fill="#fff"/></svg>
      <p class="back__phone">555-014-7281</p>
    </div>
  </article>
</section>

<section class="slot slot--spread">
  <div class="spread">
    <div class="spread__half">
      <article class="page back">
        <div class="back__photo" role="img" aria-label="Dark photograph of two business people shaking hands"></div>
        <div class="back__content">
          <h2 class="back__thanks">Thank you!</h2>
          <p class="back__company">Ferncliff Capital Management</p>
          <div class="back__rule"></div>
          <p class="back__line">desk@ferncliffcm.com</p>
          <svg class="back__icon" width="18" height="13" viewBox="0 0 18 13"><rect x="1" y="1" width="16" height="11" fill="none" stroke="#fff" stroke-width="1.4"/><path d="M1 1l8 6 8-6" fill="none" stroke="#fff" stroke-width="1.4"/></svg>
          <p class="back__line">office@ferncliffcm.com</p>
          <svg class="back__icon" width="16" height="16" viewBox="0 0 16 16"><path d="M4 1l3 3-2 2c1 2 3 4 5 5l2-2 3 3-2 3C7 15 1 9 1 3z" fill="#fff"/></svg>
          <p class="back__phone">555-014-7281</p>
        </div>
      </article>
    </div>
    <div class="spread__half">
      <article class="page cover">
        <header class="cover__header">
          <div class="brand">
            <span class="brand__mark"></span>
            <div><div class="brand__name">FERNCLIFF</div><div class="brand__sub">CAPITAL MANAGEMENT</div></div>
          </div>
          <div class="partner">
            <span class="partner__mark"></span>
            <div><div class="partner__name">QDS</div><div class="partner__sub">Quantis Data Systems</div></div>
          </div>
        </header>
        <div class="cover__photo" role="img" aria-label="Photograph looking up at glass skyscrapers against a pale sky"></div>
        <div class="cover__title-band"><h1 class="cover__title">CLEARVIEWML</h1></div>
        <footer class="cover__footer">
          <p class="cover__tagline">Bringing together expert capital management and agile predictive modeling</p>
          <div class="cover__rule"></div>
          <p class="cover__web">
            <svg width="16" height="16" viewBox="0 0 16 16"><circle cx="8" cy="8" r="7" fill="none" stroke="#d6d8dc" stroke-width="1.4"/><path d="M1 8h14M8 1c3 3 3 11 0 14M8 1c-3 3-3 11 0 14" fill="none" stroke="#d6d8dc" stroke-width="1.2"/></svg>
            www.ferncliffcm.com
          </p>
        </footer>
      </article>
    </div>
  </div>
</section>

</body>
</html>
```